Postcard for commercial concrete cleaning company that will be mailed to business customers

A 6x9 postcard that will be mailed out to businesses who have concrete (sidewalks, drive thrus, dumpster pads, etc) that need periodic pressure washing to keep clean. Our current customers are majority restaurants. We are able to remove gum and grease from concrete which is difficult for much of our competitors. We work at night when the businesses are closed or slow if 24hr.

Target Market(s)

This will go to restaurants, banks, gas stations and other retail locations.

Colors

Designer to choose colors to be used in the design.

Requirements
Must have
• Logo. A headline that mentions commercial concrete cleaning so recipients will know at a glance what we do
Nice to have
• The image included is of a fast food doorway that is half cleaned, the right side. Something like "Dirty Doorway?" may make sense.
• We specialize is maintenance concrete cleaning where we come on a regular basis so I like phrase keep your concrete clean, or keep your business clean. something like that.

```html
<!DOCTYPE html>
<html lang="en">
<head>
<meta charset="UTF-8">
<title>Ridgeline Commercial Pressure Washing – Postcard</title>
<link href="https://fonts.googleapis.com/css2?family=Lato:wght@400;700;900&display=swap" rel="stylesheet">
<style>
  :root {
    --backdrop: #2b2b2b;
    --brand-blue: #1a6bb8;
    --brand-navy: #1c2a66;
    --ink: #2f2f2f;
    --black-band: #0c0c0c;
    --white: #ffffff;
    --silver-light: #fbfbfb;
    --silver-mid: #e6e7e9;
  }
  * { margin: 0; padding: 0; box-sizing: border-box; }
  html, body { width: 920px; height: 1200px; overflow: hidden; background: var(--backdrop); }
  body { position: relative; font-family: "Lato", Arial, sans-serif; }

  .card {
    position: absolute;
    left: 80px;
    width: 759px;
    height: 506px;
    overflow: hidden;
    background:
      linear-gradient(115deg, transparent 45%, rgba(255,255,255,.7) 52%, transparent 58%),
      linear-gradient(120deg, var(--silver-light) 0%, var(--white) 35%, var(--silver-mid) 70%, var(--white) 100%);
  }
  .card--front { top: 84px; }
  .card--back  { top: 610px; }

  .logo { position: absolute; color: var(--brand-navy); font-weight: 900; }
  .logo__name { display: block; letter-spacing: -0.5px; line-height: 1; }
  .logo__tag { display: block; font-weight: 900; text-transform: uppercase; line-height: 1; }

  .card--front .logo { left: 42px; top: 60px; }
  .card--front .logo__name { font-size: 33px; }
  .card--front .logo__tag { font-size: 17px; letter-spacing: 6.4px; margin-top: 9px; }

  .headline {
    position: absolute; left: 42px; top: 160px;
    color: var(--brand-blue); font-weight: 900; font-size: 41px; line-height: 51px;
    text-transform: uppercase;
  }
  .tagline {
    position: absolute; left: 42px; top: 336px;
    color: var(--ink); font-weight: 900; font-size: 29px; line-height: 34px;
    text-transform: uppercase;
  }

  .photo-art { position: absolute; left: 0; top: 0; }

  .flag {
    position: absolute; height: 44px;
    background: var(--brand-blue); color: var(--white);
    font-weight: 700; font-size: 17px; line-height: 44px;
    text-transform: uppercase;
  }
  .flag--help { left: 580px; top: 314px; width: 179px; padding-left: 20px; clip-path: polygon(0 0, 100% 0, 100% 100%, 14px 100%); }
  .flag--question { left: 388px; top: 370px; width: 221px; padding-left: 24px; clip-path: polygon(0 0, 94% 0, 100% 100%, 0 100%); }

  .cta-bar {
    position: absolute; left: 0; top: 442px; width: 100%; height: 64px;
    background: var(--brand-blue); color: var(--white);
    font-weight: 900; font-size: 31px; line-height: 64px; text-align: center;
  }

  .card--back .logo { left: 40px; top: 50px; }
  .card--back .logo__name { font-size: 42px; }
  .card--back .logo__tag { font-size: 23px; letter-spacing: 8.6px; margin-top: 10px; }

  .services-band {
    position: absolute; left: 0; top: 157px; width: 472px; height: 51px;
    background: var(--black-band); color: var(--white);
    font-size: 18px; font-weight: 700; line-height: 51px; padding-left: 33px;
    clip-path: polygon(0 0, 93% 0, 100% 100%, 0 100%);
  }
  .benefits { position: absolute; left: 33px; top: 232px; width: 400px; color: var(--black-band); font-size: 20.5px; font-weight: 700; line-height: 23px; }
  .benefits p + p { margin-top: 23px; }

  .phone-band {
    position: absolute; left: 0; top: 393px; width: 472px; height: 74px;
    background: var(--black-band); color: var(--white);
    font-weight: 900; font-size: 58px; line-height: 74px; padding-left: 33px;
    clip-path: polygon(0 0, 100% 0, 92% 100%, 0 100%);
  }
  .base-strip { position: absolute; left: 0; top: 490px; width: 100%; height: 16px; background: var(--brand-blue); }
</style>
</head>
<body>

<section class="card card--front">
  <div class="logo">
    <span class="logo__name">Ridgeline Commercial</span>
    <span class="logo__tag">Pressure Washing</span>
  </div>

  <h1 class="headline">Commercial<br>Concrete<br>Cleaning</h1>
  <p class="tagline">First Impressions<br>Last</p>

  <svg class="photo-art" width="759" height="442" viewBox="0 0 759 442">
    <defs>
      <clipPath id="photo-shape">
        <path d="M478,0 Q300,221 430,442 L759,442 L759,0 Z"/>
      </clipPath>
      <linearGradient id="photo-tones" x1="0" y1="0" x2="0" y2="1">
        <stop offset="0" stop-color="#8e8a84"/>
        <stop offset="0.35" stop-color="#a59a86"/>
        <stop offset="0.62" stop-color="#c9bfae"/>
        <stop offset="0.75" stop-color="#4c4c4c"/>
        <stop offset="1" stop-color="#3a3a3a"/>
      </linearGradient>
    </defs>
    <rect width="759" height="442" fill="url(#photo-tones)" clip-path="url(#photo-shape)"
          role="img" aria-label="Photo of a storefront entrance with concrete walkway, half pressure-washed clean"/>
    <path d="M466,0 Q284,221 418,442" fill="none" stroke="var(--brand-blue)" stroke-width="4"/>
  </svg>

  <div class="flag flag--help">We can help!</div>
  <div class="flag flag--question">Dirty sidewalks?</div>

  <div class="cta-bar">Call for a free quote and demo 615-555-0187</div>
</section>

<section class="card card--back">
  <div class="logo">
    <span class="logo__name">Ridgeline Commercial</span>
    <span class="logo__tag">Pressure Washing</span>
  </div>

  <div class="services-band">Sidewalks | Drive Thrus | Dumpster Pads, Etc</div>

  <div class="benefits">
    <p>We are able to remove gum and grease from concrete which is difficult for many of our competitors.</p>
    <p>We work at night so your business is not interrupted.</p>
  </div>

  <div class="phone-band">615-555-0187</div>
  <div class="base-strip"></div>
</section>

</body>
</html>
```